PREMIUM Pagewall Page Design - A+++ Designers Wanted

** DO NOT ATTEMPT TO CONTACT ME THROUGH SEARCHING ON SEEKRA OR EMAILING ME THROUGH MY WEBSITE **

I need an amazing, fresh, contemporary Pagewall banner design created, using supplied photos.

You must be able to excellent graphics deisgn and photoshop skills to 'manipulate' photos to extend them / modify them for working on a horizontal banner.

Target Market(s)

Agency, Advertising Agency, Creative, Designers, Social Media, Online

Industry/Entity Type

Seekra

Font styles to use
Serif
Sans Serif

Requirements
Must have
• It must be fresh, clean, uncluttered and bold, and have text in the same font style (Arial Bold).
• Here are the photos you can download to choose from https://www.filecrate-share.example/sh/47kkwpt219qmzav/BCDnYPT1z6L5Fhyk8j1FcNcJb?dl=0
• For Text Style Sample : You can use any combination of Yellow, Black, White and Blue as per "SAMPLE UPLOAD FILE 1".
• Text : Pagewall Text must say "MAKING CENTURY OLD STORY TELLING A BRAND NEW EXPERIENCE" (see www.pagewall.example/fastlakeow for example)
• Second Project - To be awarded to winner of Pagewall project and paid additional $$
• Blurtix Text: I am open to designs and styles here. You can try any combination of "OWEN FASTLAKE" logo (see attached) and words like "GLOBAL FUTURIST" "STORY TELLER". I will leave you to design some ideas.
• The image must also be viewable on mobile & desktop, without losing any text.
• The 'profile' headshot photo for both can also be changed to suit your design.
Nice to have
• Must have a premium, fresh and uncluttered look. You should explore how to get the most out of the photos, and can edit them to create / extend the image to make it fit the banner space.
Should not have
• No funny or silly standard / off the shelf designs
• ** DO NOT ATTEMPT TO CONTACT ME THROUGH SEARCHING ON SEEKRA OR EMAILING ME THROUGH MY WEBSITE **

```html
<!DOCTYPE html>
<html lang="en">
<head>
<meta charset="utf-8">
<title>Owen Fastlake – Cover Banner</title>
<link rel="stylesheet" href="https://fonts.googleapis.com/css2?family=Arimo:wght@700&display=swap">
<style>
  :root {
    --navy-deep: #070b3a;
    --navy: #0d1a78;
    --blue-glow: #2338c9;
    --neon: #f4f6ff;
    --neon-halo: rgba(120, 150, 255, 0.75);
    --yellow: #f7bf13;
    --white: #ffffff;
    --black: #000000;
    --portrait-dark: #161a3c;
    --portrait-mid: #3a3f6e;
  }
  html, body {
    margin: 0;
    padding: 0;
    overflow: hidden;
    background: var(--navy-deep);
  }
  .banner {
    position: relative;
    width: 1200px;
    height: 444px;
    overflow: hidden;
    background:
      radial-gradient(ellipse 520px 420px at 960px 200px, var(--blue-glow) 0%, rgba(35,56,201,0) 70%),
      linear-gradient(90deg, var(--navy-deep) 0%, #0a1258 45%, var(--navy) 100%);
    font-family: "Arimo", Arial, sans-serif;
    font-weight: 700;
  }
  .neon-lines {
    position: absolute;
    inset: 0;
  }
  .portrait {
    position: absolute;
    left: 760px;
    top: 0;
    width: 360px;
    height: 444px;
    background: radial-gradient(ellipse 150px 190px at 180px 150px, var(--portrait-mid) 0%, var(--portrait-dark) 75%, rgba(22,26,60,0) 100%),
                linear-gradient(180deg, rgba(22,26,60,0) 0%, var(--portrait-dark) 60%);
  }
  .wordmark {
    position: absolute;
    left: 28px;
    top: 29px;
    margin: 0;
    font-size: 16px;
    letter-spacing: -0.2px;
    color: var(--white);
  }
  .headline {
    position: absolute;
    left: 0;
    top: 0;
    margin: 0;
  }
  .headline-line {
    position: absolute;
    display: block;
    height: 46px;
    line-height: 46px;
    background: var(--black);
    font-size: 24px;
    letter-spacing: 0.6px;
    text-align: center;
    white-space: nowrap;
  }
  .headline-line--accent {
    left: 42px;
    top: 104px;
    width: 598px;
    color: var(--yellow);
  }
  .headline-line--plain {
    left: 123px;
    top: 162px;
    width: 440px;
    height: 44px;
    line-height: 44px;
    color: var(--white);
  }
</style>
</head>
<body>
  <div class="banner">
    <svg class="neon-lines" width="1200" height="444" viewBox="0 0 1200 444" aria-hidden="true">
      <defs>
        <filter id="neon-glow" x="-50%" y="-50%" width="200%" height="200%">
          <feGaussianBlur stdDeviation="5" result="blur"/>
          <feMerge>
            <feMergeNode in="blur"/>
            <feMergeNode in="SourceGraphic"/>
          </feMerge>
        </filter>
      </defs>
      <g filter="url(#neon-glow)" stroke-linecap="round">
        <line x1="692" y1="0" x2="692" y2="404" stroke="var(--neon-halo)" stroke-width="10"/>
        <line x1="692" y1="0" x2="692" y2="404" stroke="var(--neon)" stroke-width="5"/>
        <polyline points="1088,64 1200,156" fill="none" stroke="var(--neon-halo)" stroke-width="10"/>
        <polyline points="1088,64 1200,156" fill="none" stroke="var(--neon)" stroke-width="5"/>
        <polyline points="1072,304 1200,198" fill="none" stroke="var(--neon-halo)" stroke-width="10"/>
        <polyline points="1072,304 1200,198" fill="none" stroke="var(--neon)" stroke-width="5"/>
      </g>
    </svg>

    <div class="portrait" role="img" aria-label="Portrait photo of Owen Fastlake in a dark navy jacket, lit by blue neon"></div>

    <p class="wordmark">OWENFASTLAKE</p>

    <h1 class="headline">
      <span class="headline-line headline-line--accent">MAKING CENTURY OLD STORY TELLING</span>
      <span class="headline-line headline-line--plain">A BRAND NEW EXPERIENCE</span>
    </h1>
  </div>
</body>
</html>
```